Redesign of Brochure of company services

We need a redesign a brochure. All of the content on the existing brochure correct, but the design we are not pleased with it. I will provide the previous brochure. Every Window Bright is Angolan company that provides multiple service ranging providing fruits, vegetables, fisheries, and meat to multiple industries in angola. Every Window Bright seeks to start delivering or providing their service to home owners looking for fresh products. We want a brochure design that covers all of these aspects.

Target Market(s)

Home owners, middle and upper age mothers, middle and upper class

Industry/Entity Type

Retail

Requirements
Must have
• Logo of the company and the content info
Nice to have
• It's up to you

```html
<!DOCTYPE html>
<html lang="pt">
<head>
<meta charset="utf-8">
<title>Every Window Bright – Brochura</title>
<link rel="stylesheet" href="https://fonts.googleapis.com/css2?family=Fira+Sans:wght@300;400;600;700&family=Fira+Sans+Condensed:wght@700&family=Open+Sans:wght@300;400;600;700&display=swap">
<style>
:root{
  --bg:#4f3320;
  --orange:#ef6b22;
  --orange-light:#f3852f;
  --accent:#e8521b;
  --ink:#222;
  --grey:#565656;
  --grey-light:#cfcfcf;
  --green:#7cb52a;
  --white:#fff;
}
*{margin:0;padding:0;box-sizing:border-box}
html,body{width:840px;height:1200px;overflow:hidden;background:var(--bg)}
body{position:relative;font-family:"Open Sans",sans-serif;color:var(--ink)}
.label{position:absolute;width:240px;text-align:center;color:var(--white);font-family:"Fira Sans",sans-serif;font-weight:600;font-size:25px;line-height:30px}
.spread{position:absolute;left:67px;width:714px;height:504px;background:var(--white);box-shadow:0 2px 6px rgba(0,0,0,.4);overflow:hidden}
.panel{position:absolute;width:238px;overflow:hidden}
.top{top:0;height:218px}
.bottom{top:400px;height:104px}
.band{position:absolute;left:0;width:714px;height:12px;background:var(--grey)}
.orange{background:linear-gradient(180deg,var(--orange-light),var(--orange));color:var(--white)}
.photo{position:absolute;top:230px;height:158px;width:238px}
.swoosh{position:absolute;left:0;top:0;width:714px;height:504px;pointer-events:none}
.h-orange{color:var(--accent);font-family:"Fira Sans",sans-serif;font-weight:700}
.small{font-size:7.4px;line-height:11.5px;text-align:justify}
.abs{position:absolute}
.center{text-align:center}
.nowrap{white-space:nowrap}
.light{font-family:"Fira Sans",sans-serif;font-weight:300}
.dot{display:inline-block;width:12px;height:12px;border-radius:50%;background:var(--green);margin-right:9px;vertical-align:-1px}
</style>
</head>
<body>

<div class="label" style="left:59px;top:38px">Outside flap</div>
<div class="label" style="left:301px;top:38px">Front</div>
<div class="label" style="left:541px;top:38px">Front</div>

<!-- Outside spread -->
<section class="spread" style="top:90px">
  <div class="panel top" style="left:0">
    <h2 class="h-orange abs nowrap" style="left:23px;top:14px;font-size:18px">Frescos de Qualidade</h2>
    <h3 class="abs nowrap" style="left:23px;top:52px;font-family:'Fira Sans',sans-serif;font-weight:600;font-size:14px">Confie em Qualidade</h3>
    <p class="abs" style="left:23px;top:76px;width:202px;font-size:8px;line-height:12px">A qualidade de todos os frescos distribuídos por nós é verificada para que apenas os produtos aprovados chegem até si.</p>
    <ol class="abs nowrap" style="left:23px;top:133px;list-style:none;color:var(--accent);font-weight:300;font-size:15px;line-height:25.5px">
      <li>1. Encomende por telefone</li>
      <li>2. Pague no banco</li>
      <li>3. Receba os seus frescos</li>
    </ol>
  </div>
  <div class="panel top orange center" style="left:238px">
    <h2 class="abs nowrap" style="left:0;width:238px;top:14px;font-family:'Fira Sans',sans-serif;font-weight:600;font-size:17px">Entregamos à sua porta</h2>
    <p class="abs" style="left:0;width:238px;top:56px;font-family:'Fira Sans',sans-serif;font-weight:700;font-size:19.5px;line-height:24px">Qualidade.Rapidez.<br>Satisfação</p>
    <p class="abs" style="left:0;width:238px;top:128px;font-size:14px;line-height:19.5px">Se for produtor e deseja<br>comercializar os seus<br>produtos de forma segura,<br>contacte-nos hoje!</p>
  </div>
  <div class="panel top center" style="left:476px">
    <div class="abs nowrap" style="left:0;width:238px;top:96px;display:flex;align-items:center;justify-content:center;gap:7px">
      <span style="width:14px;height:14px;background:var(--accent);display:inline-block"></span>
      <span style="font-size:19px;color:var(--ink)">Every Window Bright</span>
    </div>
    <p class="abs" style="left:0;width:238px;top:152px;color:var(--accent);font-size:14px;line-height:19.5px;font-weight:300">Levamos produtos frescos<br>Nacionais à sua porta.</p>
  </div>

  <div class="band" style="top:218px"></div>
  <div class="photo" style="left:0;background:linear-gradient(135deg,#b9302f,#d85a52 55%,#f3eee6)" role="img" aria-label="Cortes de carne vermelha fresca com salsa e alho"></div>
  <div class="photo" style="left:238px;background:linear-gradient(135deg,#c9413b,#e9d9c8 50%,#6b8f3c)" role="img" aria-label="Travessa de peixe fresco fatiado com folhas verdes"></div>
  <div class="photo" style="left:476px;background:linear-gradient(160deg,#f7f3ec,#b06a2e 45%,#c62a22 75%,#4f8f2a)" role="img" aria-label="Cesto de vime com legumes e frutas variados"></div>
  <div class="band" style="top:388px"></div>

  <div class="panel bottom" style="left:0">
    <div class="abs" style="left:16px;top:22px;width:75px;height:58px;background:var(--grey-light)"></div>
    <h3 class="h-orange abs nowrap" style="left:99px;top:22px;font-size:13.5px">Fazemos Descontos</h3>
    <p class="abs" style="left:99px;top:43px;width:135px;font-size:10.5px;line-height:13.5px">Fazemos descontos a clientes com contratos de fornecimento contínuo.</p>
  </div>
  <div class="panel bottom orange center" style="left:238px;font-family:'Fira Sans',sans-serif">
    <p class="abs nowrap" style="left:0;width:238px;top:20px;font-weight:600;font-size:12px">Manuseamos com cuidado</p>
    <p class="abs nowrap" style="left:0;width:238px;top:36px;font-weight:700;font-size:25px;line-height:32px">+244 900 410 275</p>
    <p class="abs nowrap" style="left:0;width:238px;top:74px;font-weight:600;font-size:12px">lurdes.canto@mail.ao</p>
  </div>
  <div class="panel bottom center" style="left:476px">
    <p class="abs" style="left:0;width:230px;top:12px;color:var(--accent);font-weight:300;font-size:21px;line-height:25.5px">Hortaliças<br>Frutas Carnes<br>Peixes Mariscos</p>
  </div>

  <svg class="swoosh" viewBox="0 0 714 504" aria-hidden="true">
    <path d="M476 218 L580 218 C660 218 706 190 714 130 L714 218 Z" fill="#fff"/>
    <path d="M580 218 C660 218 706 190 714 130 L714 160 C706 215 660 230 580 230 L476 230 L476 218 Z" fill="#565656"/>
    <path d="M560 400 C650 400 704 432 708 504 L714 504 L714 400 Z" fill="#fff"/>
    <path d="M560 400 C650 400 704 432 708 504 L714 504 L714 470 C700 420 650 400 600 400 Z" fill="#565656"/>
  </svg>
</section>

<!-- Inside spread -->
<section class="spread" style="top:622px">
  <div class="panel top" style="left:0">
    <h3 class="h-orange abs nowrap" style="left:22px;top:23px;font-size:13px">Hortaliças e Frutas</h3>
    <p class="small abs" style="left:22px;top:45px;width:200px">Fornecemos as mais variadas hortaliças, incluindo batata rena, batata doce, alface, abóbora, couve lombarda, couve repolho, couve repolho roxa,cebola, beterraba, beringela, courgette, nabo, feijão verde e milho.</p>
    <h3 class="h-orange abs nowrap" style="left:22px;top:123px;font-size:13px">Carnes</h3>
    <p class="small abs" style="left:22px;top:145px;width:200px">Distribuimos carne fresca de gado ovino, caprino, bovino e suíno e apostamos em produtos de elevada qualidade que nos permitam manter padrões constantes de qualidade dos produtos e dos serviços por nós prestados.</p>
  </div>
  <div class="panel top orange" style="left:238px">
    <h2 class="light abs nowrap" style="left:19px;top:14px;width:202px;font-size:21px;line-height:26px;padding-bottom:3px;border-bottom:1px solid rgba(255,255,255,.7)">Estamos abertos 24/24</h2>
    <p class="light abs nowrap" style="left:19px;top:54px;font-size:16px">Contact: +244 900 410 275</p>
    <p class="abs nowrap" style="left:19px;top:76px;font-weight:300;font-size:12px">lurdes.canto@mail.ao</p>
    <div class="abs" style="left:18px;top:104px;width:84px;height:98px;border:2px solid #fff;background:linear-gradient(160deg,#e9e1d6,#8a5a3c)" role="img" aria-label="Retrato da gerente Lurdes Canto"></div>
    <p class="abs" style="left:116px;top:104px;width:108px;font-size:7px;line-height:11px">"A nossa missão é aproximar os produtores nacionais dos seus clientes finais, garantindo qualidade e consistência."</p>
    <p class="abs nowrap" style="left:116px;top:182px;font-family:'Fira Sans',sans-serif;font-weight:700;font-size:10.5px;line-height:12.5px">Lurdes Canto<br>Gerente</p>
  </div>
  <div class="panel top" style="left:476px">
    <p class="abs nowrap" style="left:17px;top:14px;font-size:15.5px;line-height:19.5px">Trazemos frescos da<br>melhor qualidade a bom<br>preço direitinho à sua porta.</p>
    <ul class="abs nowrap" style="left:17px;top:88px;list-style:none;display:grid;grid-template-columns:112px 90px;row-gap:1px;font-family:'Fira Sans',sans-serif;font-weight:600;font-size:14px;line-height:17.5px;color:var(--accent)">
      <li><span class="dot"></span>Hortaliças</li>
      <li><span class="dot"></span>Frutas</li>
      <li><span class="dot"></span>Carnes</li>
      <li><span class="dot"></span>Peixes</li>
      <li><span class="dot"></span>Mariscos</li>
    </ul>
    <p class="abs nowrap" style="left:17px;top:154px;font-size:14.5px;line-height:18.5px">Não viu o que procura?<br>Ligue já para<br>o 900 410 275</p>
  </div>

  <div class="band" style="top:218px"></div>
  <div class="photo" style="left:0;background:linear-gradient(160deg,#8fbf3a,#d23a22 40%,#e8a03c 70%,#c08a4a)" role="img" aria-label="Cesto de legumes com pimentos, tomates e beringela"></div>
  <div class="photo" style="left:238px;background:linear-gradient(135deg,#6a2f5a,#d13b2a 30%,#f2c12e 55%,#5c9a2c 80%)" role="img" aria-label="Variedade de frutas e legumes frescos"></div>
  <div class="photo" style="left:476px;background:linear-gradient(180deg,#e4edf3,#f6f0c8 30%,#b8cf4a 55%,#7fa22a)" role="img" aria-label="Campo verde de cultivo ao nascer do sol"></div>
  <div class="band" style="top:388px"></div>

  <div class="panel bottom" style="left:0">
    <h3 class="h-orange abs nowrap" style="left:22px;top:16px;font-size:13px">Peixes e Mariscos</h3>
    <p class="small abs" style="left:22px;top:38px;width:200px">Dispomos de uma vasta gama de peixes e mariscos incluindo pescada, salmão, bacalhau, atum, sardinha, carapau, linguado, camarão, lagostim, gambas, entre outros. Fornecemos o peixe e marisco sempre frescos.</p>
  </div>
  <div class="panel bottom orange center" style="left:238px">
    <p class="light abs nowrap" style="left:0;width:238px;top:14px;font-size:19px">Every Window Bright Corp</p>
    <p class="light abs nowrap" style="left:0;width:238px;top:44px;font-size:17px;line-height:22.5px">Estamos no Bairro Azul<br>Luanda, Angola.</p>
  </div>
  <div class="panel bottom" style="left:476px">
    <h3 class="abs nowrap" style="left:16px;top:24px;font-family:'Fira Sans Condensed',sans-serif;font-weight:700;font-size:20px;color:var(--accent)">PRODUTOS NACIONAIS</h3>
    <p class="abs nowrap" style="left:16px;top:59px;font-size:12.5px;line-height:17px">Vendemos apenas produtos<br>nacionais de qualidade controlada</p>
  </div>

  <svg class="swoosh" viewBox="0 0 714 504" aria-hidden="true">
    <path d="M476 218 L580 218 C660 218 706 190 714 130 L714 218 Z" fill="#fff"/>
    <path d="M580 218 C660 218 706 190 714 130 L714 160 C706 215 660 230 580 230 L476 230 L476 218 Z" fill="#565656"/>
    <path d="M560 400 C650 400 704 432 708 504 L714 504 L714 470 C700 420 650 400 600 400 Z" fill="#565656"/>
  </svg>
</section>

<div class="label" style="left:69px;top:1137px">Inside Left</div>
<div class="label" style="left:310px;top:1137px">Inside Center</div>
<div class="label" style="left:550px;top:1137px">Inside Right</div>

</body>
</html>
```